Verndale Harbor Partners

Please look at the logo that we've just received and based on it provide us with the business card designs.

Industry/Entity Type

Business

Requirements
Must have
• Dummy text, so later on we can add the exact names and titles.

```html
<!DOCTYPE html>
<html lang="en">
<head>
<meta charset="utf-8">
<title>Verndale Harbor Partners – Business Cards</title>
<link rel="stylesheet" href="https://fonts.googleapis.com/css2?family=Montserrat:ital,wght@0,400;0,600;0,700;1,400&family=Barlow+Semi+Condensed:ital,wght@0,400;0,600;1,400&display=swap">
<style>
  :root {
    --navy: #233468;
    --blue: #2f63b8;
    --paper: #ffffff;
    --stage: #e9e7e4;
  }
  * { box-sizing: border-box; margin: 0; padding: 0; }
  html, body { width: 1200px; height: 1200px; overflow: hidden; }
  body {
    background: var(--stage);
    font-family: "Montserrat", sans-serif;
    color: var(--navy);
    position: relative;
  }
  .card {
    position: absolute;
    width: 523px;
    height: 299px;
    background: var(--paper);
    overflow: hidden;
    box-shadow: 0 3px 10px rgba(0,0,0,0.18);
  }
  .card--one   { left: 54px;  top: 110px; }
  .card--two   { left: 622px; top: 110px; }
  .card--three { left: 54px;  top: 450px; }
  .card--four  { left: 622px; top: 450px; }
  .card--five  { left: 54px;  top: 790px; }
  .card--six   { left: 622px; top: 790px; }

  .card__shapes { position: absolute; inset: 0; width: 523px; height: 299px; }
  .panel { position: absolute; top: 0; height: 299px; background: var(--navy); }

  .wordmark {
    position: absolute;
    display: flex;
    align-items: center;
    gap: 10px;
  }
  .wordmark__square { width: 16px; height: 16px; background: var(--navy); flex: none; }
  .wordmark__name {
    font-family: "Montserrat", sans-serif;
    font-weight: 600;
    color: var(--navy);
    font-size: 27px;
    line-height: 1.05;
    text-transform: uppercase;
    letter-spacing: 0.5px;
    white-space: nowrap;
  }
  .wordmark--small .wordmark__name { font-size: 21px; }
  .wordmark--small .wordmark__square { width: 13px; height: 13px; }
  .wordmark--compact .wordmark__name { font-size: 18px; }
  .wordmark--compact .wordmark__square { width: 12px; height: 12px; }

  .person { position: absolute; text-align: right; }
  .person__name { font-weight: 700; font-size: 15px; line-height: 1.25; }
  .person__title { font-style: italic; font-size: 13px; line-height: 1.3; }

  .contact { position: absolute; font-size: 15px; line-height: 19px; white-space: nowrap; }
  .contact b { font-weight: 700; }
  .contact--right { text-align: right; }
  .contact--light { color: #fff; }
  .light { color: #fff; }

  .condensed { font-family: "Barlow Semi Condensed", sans-serif; }
  .condensed .person__name { font-weight: 600; font-size: 16px; }

  .glow { position: absolute; }

  .icon-row { display: flex; justify-content: flex-end; align-items: center; gap: 8px; height: 22px; }
  .icon-row svg { width: 15px; height: 15px; flex: none; }
</style>
</head>
<body>

  <!-- Card 1: fleck panel with diagonal navy band -->
  <section class="card card--one">
    <svg class="card__shapes" viewBox="0 0 523 299" aria-hidden="true">
      <defs>
        <pattern id="fleck" width="6" height="6" patternUnits="userSpaceOnUse">
          <rect width="6" height="6" fill="#f3f3f3"/>
          <circle cx="1.5" cy="2" r="0.8" fill="#dcdcdc"/>
          <circle cx="4.5" cy="4.6" r="0.7" fill="#e2e2e2"/>
        </pattern>
      </defs>
      <polygon points="0,0 462,0 274,190 0,190" fill="url(#fleck)"/>
      <polygon points="0,190 274,190 382,299 0,299" fill="var(--navy)"/>
    </svg>
    <div class="wordmark" style="left:22px; top:74px;">
      <span class="wordmark__square"></span>
      <span class="wordmark__name">Verndale Harbor<br>Partners</span>
    </div>
    <div class="person" style="right:23px; top:112px;">
      <div class="person__name">Alex Moran</div>
      <div class="person__title">Director</div>
    </div>
    <div class="contact contact--right" style="right:23px; top:158px; font-size:14px;">
      <b>m:</b> 123 456-789<br>
      <b>e:</b> am@verndaleharbor.com
    </div>
    <div class="contact contact--light" style="left:18px; top:208px;">
      Location XXX, XXX, Canada XXXX<br>
      <b>p:</b> 123 456-789<br>
      <b>e:</b> info@verndaleharbor.com<br>
      <b>w:</b> verndaleharbor.com
    </div>
  </section>

  <!-- Card 2: white top, navy and blue split band -->
  <section class="card card--two condensed">
    <svg class="card__shapes" viewBox="0 0 523 299" aria-hidden="true">
      <defs>
        <linearGradient id="crease" x1="0" y1="0" x2="1" y2="0">
          <stop offset="0" stop-color="#e6e6e6"/>
          <stop offset="1" stop-color="#ffffff"/>
        </linearGradient>
      </defs>
      <polygon points="268,190 458,0 470,0 280,190" fill="url(#crease)" opacity="0.8"/>
      <polygon points="0,190 268,190 374,299 0,299" fill="var(--navy)"/>
      <polygon points="268,190 523,190 523,299 374,299" fill="var(--blue)"/>
    </svg>
    <div class="glow" role="img" aria-label="Soft light accent on blue band" style="left:330px; top:190px; width:193px; height:109px; background: radial-gradient(circle at 50% 60%, rgba(150,170,230,0.55), rgba(47,99,184,0) 65%);"></div>
    <div class="wordmark" style="left:22px; top:78px;">
      <span class="wordmark__square"></span>
      <span class="wordmark__name">Verndale Harbor<br>Partners</span>
    </div>
    <div class="person" style="right:23px; top:95px;">
      <div class="person__name">Alex Moran</div>
      <div class="person__title">Director</div>
    </div>
    <div class="contact contact--right" style="right:23px; top:139px; font-size:16px;">
      <b>m:</b> 1234 567 890<br>
      <b>e:</b> am@verndaleharbor.com
    </div>
    <div class="contact contact--light" style="left:18px; top:209px; font-size:16px;">
      Location XXX, XXX, Canada XXXX<br>
      <b>p:</b> 123 456-789<br>
      <b>e:</b> info@verndaleharbor.com<br>
      <b>w:</b> verndaleharbor.com
    </div>
  </section>

  <!-- Card 3: centred name on soft vignette -->
  <section class="card card--three" style="background: radial-gradient(ellipse 75% 80% at 45% 40%, #ffffff 45%, #e4e6f1 80%, #b9bdd8 100%);">
    <div class="wordmark" style="left:0; right:0; top:78px; justify-content:center;">
      <span class="wordmark__square"></span>
      <span class="wordmark__name" style="font-size:31px;">Verndale Harbor<br>Partners</span>
    </div>
    <div class="person" style="left:18px; top:204px; text-align:left;">
      <div class="person__name">Alex Moran</div>
      <div class="person__title">Director</div>
    </div>
    <div class="contact contact--right" style="right:18px; top:204px;">
      Location XXX, XXX, Canada<br>
      <b>P:</b> 123 456-789<br>
      <b>E:</b> info@verndaleharbor.com<br>
      <b>W:</b> verndaleharbor.com
    </div>
  </section>

  <!-- Card 4: white half, navy half -->
  <section class="card card--four">
    <div class="panel" style="left:285px; width:238px;"></div>
    <div class="glow" role="img" aria-label="Faint light accent on navy panel" style="left:330px; top:30px; width:193px; height:190px; background: radial-gradient(circle at 85% 50%, rgba(120,130,190,0.5), rgba(35,52,104,0) 60%);"></div>
    <div class="wordmark wordmark--small" style="left:22px; top:128px;">
      <span class="wordmark__square"></span>
      <span class="wordmark__name">Verndale Harbor<br>Partners</span>
    </div>
    <div class="person light" style="right:18px; top:16px;">
      <div class="person__name">Alex Moran</div>
      <div class="person__title">Director</div>
    </div>
    <div class="contact contact--right contact--light" style="right:18px; top:212px; font-size:14px;">
      Location XXX, XXX, Canada<br>
      <b>P:</b> 123 456-789<br>
      <b>E:</b> info@verndaleharbor.com<br>
      <b>W:</b> verndaleharbor.com
    </div>
  </section>

  <!-- Card 5: white left, navy right with icon list -->
  <section class="card card--five">
    <div class="panel" style="left:262px; width:261px;"></div>
    <div class="glow" role="img" aria-label="Bright light accent along panel edge" style="left:262px; top:40px; width:140px; height:220px; background: radial-gradient(ellipse at 10% 55%, rgba(255,255,255,0.85), rgba(255,255,255,0) 60%);"></div>
    <div class="wordmark wordmark--compact" style="left:24px; top:131px;">
      <span class="wordmark__square"></span>
      <span class="wordmark__name">Verndale Harbor<br>Partners</span>
    </div>
    <div class="person light" style="right:18px; top:137px;">
      <div class="person__name">Alex Moran</div>
      <div class="person__title">Director</div>
    </div>
    <div class="contact contact--light" style="right:18px; top:196px; font-size:14px;">
      <div class="icon-row">
        <svg viewBox="0 0 16 16" aria-hidden="true"><path d="M8 1a5 5 0 0 0-5 5c0 4 5 9 5 9s5-5 5-9a5 5 0 0 0-5-5zm0 7a2 2 0 1 1 0-4 2 2 0 0 1 0 4z" fill="#fff"/></svg>
        <span>Location XXX, XXX, Canada</span>
      </div>
      <div class="icon-row">
        <svg viewBox="0 0 16 16" aria-hidden="true"><path d="M5 1.5 3 2.5c-1 2 0 7 5 11l2-1-2-3-1.3.6C5.5 8.5 5 7 5 5.6L6.4 5z" fill="#fff"/></svg>
        <span>123 456-789</span>
      </div>
      <div class="icon-row">
        <svg viewBox="0 0 16 16" aria-hidden="true"><rect x="1.5" y="3.5" width="13" height="9" fill="none" stroke="#fff" stroke-width="1.4"/><path d="M1.5 3.5 8 9l6.5-5.5" fill="none" stroke="#fff" stroke-width="1.4"/></svg>
        <span>info@verndaleharbor.com</span>
      </div>
      <div class="icon-row">
        <svg viewBox="0 0 16 16" aria-hidden="true"><circle cx="8" cy="8" r="6.5" fill="none" stroke="#fff" stroke-width="1.2"/><ellipse cx="8" cy="8" rx="3" ry="6.5" fill="none" stroke="#fff" stroke-width="1.2"/><path d="M1.5 8h13M2.5 4.8h11M2.5 11.2h11" stroke="#fff" stroke-width="1.2"/></svg>
        <span>www.verndaleharbor.com</span>
      </div>
    </div>
  </section>

  <!-- Card 6: white left, navy right with pale glow across seam -->
  <section class="card card--six">
    <div class="panel" style="left:285px; width:238px;"></div>
    <div class="glow" role="img" aria-label="Pale light accent across panel seam" style="left:200px; top:40px; width:200px; height:200px; background: radial-gradient(circle at 50% 50%, rgba(201,213,235,0.95), rgba(201,213,235,0) 60%);"></div>
    <div class="wordmark wordmark--small" style="left:22px; top:130px;">
      <span class="wordmark__square"></span>
      <span class="wordmark__name">Verndale Harbor<br>Partners</span>
    </div>
    <div class="person light" style="right:18px; top:16px;">
      <div class="person__name">Alex Moran</div>
      <div class="person__title">Director</div>
    </div>
    <div class="contact contact--right contact--light" style="right:18px; top:212px; font-size:14px;">
      Location XXX, XXX, Canada<br>
      <b>P:</b> 123 456-789<br>
      <b>E:</b> info@verndaleharbor.com<br>
      <b>W:</b> verndaleharbor.com
    </div>
  </section>

</body>
</html>
```